Need to create a website for a luxury custom home builder in Phoenix USA. Looking forward for some creative designs including a full page video intro on homepage and should show up pretty luxurious.

```html
<!DOCTYPE html>
<html lang="en">
<head>
<meta charset="utf-8">
<title>Sunvale Homes</title>
<link href="https://fonts.googleapis.com/css2?family=Krona+One&family=Roboto:wght@400;500;700&family=Open+Sans:wght@400;600&display=swap" rel="stylesheet">
<style>
:root{
  --teal:#14ab8c;
  --blue:#1aa3d9;
  --ink:#1a1a1a;
  --text:#555;
  --light:#f4f4f4;
  --dark:#0b0d10;
  --white:#fff;
}
*{margin:0;padding:0;box-sizing:border-box}
html,body{width:1200px;height:4601px;overflow:hidden}
body{position:relative;font-family:"Roboto",sans-serif;color:var(--text);background:var(--white)}
.abs{position:absolute}
h2.section-title{position:absolute;font-family:"Krona One",sans-serif;font-weight:400;color:var(--ink);font-size:40px;letter-spacing:4px;line-height:1}
.btn{position:absolute;background:var(--teal);color:var(--white);font:700 13px "Roboto",sans-serif;display:flex;align-items:center;justify-content:center;letter-spacing:.3px}

/* header */
.site-header{position:absolute;left:0;top:0;width:1200px;height:80px;background:var(--white);z-index:3}
.brand{position:absolute;left:111px;top:18px;display:flex;align-items:center;gap:10px}
.brand-dot{width:30px;height:30px;border-radius:50%;background:var(--blue)}
.brand-name{font:700 24px "Roboto",sans-serif;color:var(--blue);letter-spacing:1px;line-height:1}
.brand-sub{font:700 10px "Roboto",sans-serif;color:var(--blue);letter-spacing:4px;text-align:center}
.nav a{position:absolute;top:29px;font-size:13px;color:var(--ink);text-decoration:none}
.nav a.active{color:var(--teal)}
.call-box{position:absolute;left:857px;top:0;width:343px;height:80px;background:var(--blue);clip-path:polygon(30px 0,100% 0,100% 100%,0 100%);color:var(--white)}
.call-box .label{position:absolute;left:103px;top:21px;font-size:12px}
.call-box .num{position:absolute;left:103px;top:38px;font-size:21px;font-weight:700}
.call-box svg{position:absolute;left:58px;top:25px}

/* hero */
.hero{position:absolute;left:0;top:80px;width:1200px;height:796px}
.hero-photo{position:absolute;inset:0;background:linear-gradient(180deg,#4b5157 0%,#2b2f33 45%,#1f2a22 100%)}
.hero-shape{position:absolute;left:0;top:0}
.hero-title{position:absolute;left:0;top:246px;width:1200px;text-align:center;font:400 68px "Krona One",sans-serif;color:var(--white);letter-spacing:6px}
.hero-text{position:absolute;left:0;top:332px;width:1200px;text-align:center;color:var(--white);font-size:14px;line-height:21px}

/* about */
.about-text{position:absolute;left:111px;width:466px;font-size:13px;line-height:21.4px;text-align:justify;color:var(--text)}
.about-frame{position:absolute;left:959px;top:979px;width:168px;height:150px;border:7px solid var(--teal)}
.about-photo{position:absolute;left:625px;top:1018px;width:464px;height:416px;background:linear-gradient(160deg,#8a9aa8,#6d6a63 55%,#4f7a36)}

/* services */
.services{position:absolute;left:0;top:1538px;width:1200px;height:569px;background:var(--light)}
.services-photo{position:absolute;left:0;top:0;width:493px;height:569px;background:linear-gradient(180deg,#c9d6e0 0%,#4f6275 45%,#5a6a4a 100%)}
.service{position:absolute;left:564px;width:525px}
.service svg{position:absolute;left:0;top:0}
.service h3{position:absolute;left:86px;top:0;font:500 16px "Roboto",sans-serif;color:var(--ink)}
.service p{position:absolute;left:86px;top:30px;font-size:13px;line-height:21px;width:340px}
.divider{position:absolute;left:564px;width:525px;height:1px;background:#ddd}

/* featured */
.card{position:absolute;top:2282px;width:370px}
.card-photo{height:231px}
.card h3{position:absolute;top:242px;left:0;font:500 20px "Roboto",sans-serif;color:var(--ink)}
.card .price{position:absolute;top:242px;right:0;font:700 20px "Roboto",sans-serif;color:var(--teal)}
.card p{position:absolute;top:282px;left:0;font-size:13px;line-height:21px;width:360px}
.card a{position:absolute;top:331px;left:0;font:700 13px "Roboto",sans-serif;color:var(--blue)}
.arrow-btn{position:absolute;top:2683px;width:28px;height:28px;border-radius:50%;background:#e6e6e6;display:flex;align-items:center;justify-content:center}

/* living */
.living{position:absolute;left:0;top:2816px;width:1200px;height:440px;background:linear-gradient(180deg,#1aa3d9,#2a8fc4)}
.living-title{top:2905px;left:0;width:1200px;text-align:center;color:var(--white)!important}
.living-text{position:absolute;left:200px;top:2980px;width:800px;text-align:center;color:var(--white);font-size:13px;line-height:21.5px}
.testimonial{position:absolute;left:111px;top:3102px;width:978px;height:297px;background:var(--teal)}
.testimonial-photo{position:absolute;left:23px;top:22px;width:250px;height:250px;background:linear-gradient(180deg,#c98aa6,#6f7f96 50%,#3b2f28)}
.testimonial p{position:absolute;left:312px;top:42px;width:610px;color:var(--white);font-size:12.8px;line-height:21.5px}
.stars{position:absolute;left:312px;top:222px;color:var(--white);font-size:14px;letter-spacing:4px}
.author{position:absolute;right:56px;top:226px;color:var(--white);font-size:12.5px}

/* contact */
.field{position:absolute;border:1px solid #ccc;font-size:12px;color:#777;padding:14px 18px}

/* footer */
.footer-photo{position:absolute;left:0;top:4090px;width:1200px;height:511px;background:linear-gradient(180deg,#050607,#15181b 60%,#2a2a26)}
.footer-brand{position:absolute;left:0;top:4170px;width:1200px;text-align:center;color:var(--teal)}
.footer-brand .dot{width:44px;height:44px;border-radius:50%;background:var(--blue);margin:0 auto 10px}
.footer-brand .name{font:700 28px "Open Sans",sans-serif;letter-spacing:1px;line-height:1}
.footer-brand .sub{font:600 12px "Open Sans",sans-serif;letter-spacing:5px;color:var(--blue)}
.contact-item{position:absolute;top:4298px;width:300px;text-align:center;color:var(--white);font-family:"Open Sans",sans-serif}
.contact-item .icon{width:56px;height:56px;border-radius:50%;background:var(--blue);margin:0 auto 8px;display:flex;align-items:center;justify-content:center}
.contact-item h4{font-weight:400;font-size:17px;margin-bottom:6px}
.contact-item p{font-size:13px;line-height:21px}
.copyright{position:absolute;left:0;top:4522px;width:1200px;text-align:center;color:var(--white);font:400 14px "Open Sans",sans-serif}
</style>
</head>
<body>

<header class="site-header">
  <div class="brand">
    <div class="brand-dot"></div>
    <div><div class="brand-name">SUNVALE</div><div class="brand-sub">HOMES</div></div>
  </div>
  <nav class="nav">
    <a class="active" style="left:461px">Home</a>
    <a style="left:532px">About</a>
    <a style="left:603px">Services</a>
    <a style="left:688px">Blog</a>
    <a style="left:750px">Contact</a>
  </nav>
  <div class="call-box">
    <svg width="30" height="30" viewBox="0 0 24 24"><path fill="#fff" d="M6.6 10.8a15 15 0 0 0 6.6 6.6l2.2-2.2c.3-.3.7-.4 1-.2 1.1.4 2.3.6 3.6.6.6 0 1 .4 1 1V20c0 .6-.4 1-1 1A17 17 0 0 1 3 4c0-.6.4-1 1-1h3.5c.6 0 1 .4 1 1 0 1.3.2 2.5.6 3.6.1.3 0 .7-.2 1z"/></svg>
    <div class="label">Call Us Today :</div>
    <div class="num">+1 888 888 8888</div>
  </div>
</header>

<section class="hero">
  <div class="hero-photo" role="img" aria-label="Large modern custom home at dusk with lit windows and landscaped lawn"></div>
  <h1 class="hero-title">SUNVALE</h1>
  <p class="hero-text">Lorem ipsum dolor sit amet, consectetur adipiscing elit, sed do eiusmod tempor incididunt<br>ut labore et dolore magna aliqua.</p>
  <div class="btn" style="left:527px;top:393px;width:152px;height:41px">GET STARTED</div>
  <svg class="hero-shape" width="1200" height="796" viewBox="0 0 1200 796">
    <polygon fill="#fff" points="0,643 200,559 600,796 1000,559 1200,643 1200,796 0,796"/>
    <polygon fill="#14ab8c" points="200,559 600,796 1000,559 1000,575 600,770 200,575"/>
    <polygon fill="#fff" points="200,575 600,770 1000,575 1000,596 600,740 200,596" opacity="0"/>
    <circle cx="600" cy="649" r="28" fill="#1aa3d9" stroke="#0d6e96" stroke-width="3"/>
    <polygon fill="#fff" points="593,638 593,660 610,649"/>
  </svg>
</section>

<h2 class="section-title" style="left:111px;top:1014px">ABOUT US</h2>
<p class="about-text" style="top:1074px">Lorem ipsum dolor sit amet, consectetur adipiscing elit, sed do eiusmod tempor incididunt ut labore et dolore magna aliqua. Ut enim ad minim veniam, quis nostrud exercitation ullamco laboris nisi ut aliquip ex ea commodo consequat. Duis aute irure dolor in reprehenderit in voluptate velit esse cillum dolore eu fugiat nulla pariatur.</p>
<p class="about-text" style="top:1202px">Excepteur sint occaecat cupidatat non proident, sunt in culpa qui officia deserunt mollit anim id est laborum. Lorem ipsum dolor sit amet, consectetur adipiscing elit, sed do eiusmod tempor incididunt ut labore et dolore magna aliqua. Ut enim ad minim veniam, quis nostrud exercitation ullamco laboris nisi ut aliquip ex ea commodo consequat. Duis aute irure dolor in reprehenderit in voluptate velit esse cillum dolore eu fugiat nulla pariatur. Excepteur sint occaecat cupidatat non proident, sunt in culpa qui officia deserunt mollit anim id est laborum.</p>
<div class="btn" style="left:111px;top:1393px;width:151px;height:41px">LEARN MORE</div>
<div class="about-frame"></div>
<div class="about-photo" role="img" aria-label="Stone-faced luxury house with dark slate roof and green lawn"></div>

<section class="services">
  <div class="services-photo" role="img" aria-label="Blue-sided family home with wooden porch and front steps"></div>
  <h2 class="section-title" style="left:564px;top:94px">OUR SERVICES</h2>
  <div class="service" style="top:170px">
    <svg width="70" height="70" viewBox="0 0 70 70" fill="none" stroke="#14ab8c" stroke-width="2"><path d="M8 34 30 12l22 22"/><path d="M14 28v34h32V28"/><rect x="24" y="42" width="12" height="20"/><rect x="20" y="30" width="8" height="8"/><rect x="34" y="30" width="8" height="8"/><rect x="46" y="46" width="18" height="16"/></svg>
    <h3>Duis aute irure dolor</h3>
    <p>Lorem ipsum dolor sit amet, consectetur adipiscing elit, sed do eiusmod tempor incididunt ut</p>
  </div>
  <div class="divider" style="top:266px"></div>
  <div class="service" style="top:283px">
    <svg width="76" height="70" viewBox="0 0 76 70" fill="none" stroke="#14ab8c" stroke-width="2"><path d="M24 22 42 6l18 16"/><path d="M28 20v18h28V20"/><rect x="38" y="26" width="8" height="12"/><path d="M4 50l12-6c6-2 10 0 16 2h12c3 0 3 5 0 5H32"/><path d="M44 51l16-8c4-2 7 2 3 5L42 62H20L4 66"/></svg>
    <h3>Duis aute irure dolor</h3>
    <p>Lorem ipsum dolor sit amet, consectetur adipiscing elit, sed do eiusmod tempor incididunt ut</p>
  </div>
  <div class="divider" style="top:378px"></div>
  <div class="service" style="top:395px">
    <svg width="70" height="70" viewBox="0 0 70 70" fill="none" stroke="#14ab8c" stroke-width="2"><path d="M8 32 34 8l26 24"/><path d="M14 26v38h40V26"/><rect x="44" y="8" width="6" height="12"/><rect x="22" y="36" width="24" height="20"/><path d="M34 36v20M22 46h24"/></svg>
    <h3>Duis aute irure dolor</h3>
    <p>Lorem ipsum dolor sit amet, consectetur adipiscing elit, sed do eiusmod tempor incididunt ut</p>
  </div>
</section>

<h2 class="section-title" style="left:111px;top:2207px">FEATURED PROPERTIES</h2>
<article class="card" style="left:21px">
  <div class="card-photo" role="img" aria-label="White modern villa with glass walls and garden" style="background:linear-gradient(180deg,#8fc0e6,#d8dcd8 55%,#5d8a3e)"></div>
  <h3>Duis aute irure dolor</h3><span class="price">$502.00</span>
  <p>Lorem ipsum dolor sit amet, consectetur adipiscing elit, sed do eiusmod</p>
  <a>View Details »</a>
</article>
<article class="card" style="left:418px">
  <div class="card-photo" role="img" aria-label="Contemporary dark two-storey home lit at dusk" style="background:linear-gradient(180deg,#3e4650,#2a2c2e 55%,#7a6a55)"></div>
  <h3>Duis aute irure dolor</h3><span class="price">$502.00</span>
  <p>Lorem ipsum dolor sit amet, consectetur adipiscing elit, sed do eiusmod</p>
  <a>View Details »</a>
</article>
<article class="card" style="left:813px">
  <div class="card-photo" role="img" aria-label="White farmhouse with porch surrounded by trees" style="background:linear-gradient(180deg,#9ab38a,#cfd2cf 50%,#5a8a38)"></div>
  <h3>Duis aute irure dolor</h3><span class="price">$502.00</span>
  <p>Lorem ipsum dolor sit amet, consectetur adipiscing elit, sed do eiusmod</p>
  <a>View Details »</a>
</article>
<div class="arrow-btn" style="left:564px"><svg width="10" height="10" viewBox="0 0 10 10"><path d="M7 1 3 5l4 4" fill="none" stroke="#333" stroke-width="1.6"/></svg></div>
<div class="arrow-btn" style="left:606px"><svg width="10" height="10" viewBox="0 0 10 10"><path d="M3 1l4 4-4 4" fill="none" stroke="#333" stroke-width="1.6"/></svg></div>

<section class="living" role="img" aria-label="Blue-tinted photo of a suburban home behind the section"></section>
<h2 class="section-title living-title">LIVING THE DREAM</h2>
<p class="living-text">Lorem ipsum dolor sit amet, consectetur adipiscing elit, sed do eiusmod tempor incididunt ut labore et dolore magna aliqua. Ut enim ad minim veniam, quis nostrud exercitation ullamco laboris nisi ut aliquip ex ea commodo consequat. Duis aute irure dolor in reprehenderit in voluptate velit esse cillum dolore eu fugiat nulla pariatur. Excepteur sint occaecat cupidatat non proident, sunt in culpa qui officia deserunt mollit anim id est laborum.</p>
<div class="testimonial">
  <div class="testimonial-photo" role="img" aria-label="Two-storey house with lit porch under a pink evening sky"></div>
  <p>Lorem ipsum dolor sit amet, consectetur adipiscing elit, sed do eiusmod tempor incididunt ut labore et dolore magna aliqua. Ut enim ad minim veniam, quis nostrud exercitation ullamco laboris nisi ut aliquip ex ea commodo consequat. Duis aute irure dolor in reprehenderit in voluptate velit esse cillum dolore eu fugiat nulla pariatur. Excepteur sint occaecat cupidatat non proident, sunt in culpa qui officia deserunt mollit anim id est laborum. Duis aute irure dolor in reprehenderit in voluptate velit esse cillum dolore eu fugiat nulla pariatur. Excepteur sint occaecat cupidatat non proident, sunt in culpa qui officia deserunt mollit anim id est laborum.</p>
  <div class="stars">☆☆☆☆☆</div>
  <div class="author">John Doe &nbsp;|&nbsp; Company name</div>
</div>

<h2 class="section-title" style="left:0;top:3516px;width:1200px;text-align:center">CONTACT US</h2>
<div class="field" style="left:221px;top:3581px;width:242px;height:46px">Name</div>
<div class="field" style="left:475px;top:3581px;width:243px;height:46px">Email</div>
<div class="field" style="left:730px;top:3581px;width:242px;height:46px">Phone</div>
<div class="field" style="left:221px;top:3643px;width:751px;height:115px">Message</div>
<div class="btn" style="left:477px;top:3774px;width:241px;height:43px;font-size:12px">SUBMIT NOW</div>

<footer>
  <div class="footer-photo" role="img" aria-label="Dark photo of a neighbourhood of houses at night"></div>
  <svg class="abs" style="left:0;top:3930px" width="1200" height="250" viewBox="0 0 1200 250">
    <polygon fill="#1aa3d9" points="200,242 600,6 1000,242"/>
    <polygon fill="#0b0d10" points="260,242 600,50 940,242"/>
  </svg>
  <div class="footer-brand">
    <div class="dot"></div>
    <div class="name">SUNVALE</div>
    <div class="sub">HOMES</div>
  </div>
  <div class="contact-item" style="left:121px">
    <div class="icon"><svg width="24" height="24" viewBox="0 0 24 24" fill="none" stroke="#fff" stroke-width="1.6"><path d="M12 22s7-7 7-12a7 7 0 0 0-14 0c0 5 7 12 7 12z"/><circle cx="12" cy="10" r="2.5"/></svg></div>
    <h4>Address :</h4>
    <p>123, Lorem ipsum dolor sit<br>amet, consectetur</p>
  </div>
  <div class="contact-item" style="left:447px">
    <div class="icon"><svg width="24" height="24" viewBox="0 0 24 24"><path fill="#fff" d="M6.6 10.8a15 15 0 0 0 6.6 6.6l2.2-2.2c.3-.3.7-.4 1-.2 1.1.4 2.3.6 3.6.6.6 0 1 .4 1 1V20c0 .6-.4 1-1 1A17 17 0 0 1 3 4c0-.6.4-1 1-1h3.5c.6 0 1 .4 1 1 0 1.3.2 2.5.6 3.6.1.3 0 .7-.2 1z"/></svg></div>
    <h4>Phone :</h4>
    <p style="font-size:16px">+1 888 888 8888</p>
  </div>
  <div class="contact-item" style="left:777px">
    <div class="icon"><svg width="24" height="24" viewBox="0 0 24 24" fill="none" stroke="#fff" stroke-width="1.6"><rect x="3" y="6" width="18" height="12"/><path d="M3 6l9 7 9-7"/></svg></div>
    <h4>Email address :</h4>
    <p>info@companyname.com</p>
  </div>
  <div class="copyright">© Copyrights 2023 Company name | All Rights Reserved</div>
</footer>

</body>
</html>
```